Zielgruppe
Herstellung und Vertrieb von Baustoffen als Eigenmarke
Aufgabenstellung
Wiedererkennungswert unserer Marke. Technisches Verständniss für die Umsetrzung. Klares Design. Logo muss mit eingebaut werden. Rundes etikett mit Durchmesser 18 cm.

```html
<!DOCTYPE html>
<html lang="de">
<head>
<meta charset="utf-8">
<title>Bitumen Alu Dichtband – Rundetikett</title>
<link rel="stylesheet" href="https://fonts.googleapis.com/css2?family=Lato:wght@400;700&family=Montserrat:wght@300;700&family=Open+Sans:wght@400&family=Varela+Round&display=swap">
<style>
  :root {
    --label-black: #000000;
    --paper-white: #ffffff;
    --ring-grey: #c8c7c8;
    --brand-orange: #e4501f;
    --tape-sand: #bba594;
    --tape-brown: #5f4242;
    --text-dark: #1a1410;
  }
  html, body {
    margin: 0;
    padding: 0;
    width: 1200px;
    height: 1200px;
    overflow: hidden;
    background: var(--paper-white);
  }
  .label { display: block; width: 1200px; height: 1200px; }
  .company-name { font-family: "Lato", sans-serif; font-weight: 700; font-size: 15px; fill: var(--brand-orange); }
  .company-contact { font-family: "Lato", sans-serif; font-weight: 400; font-size: 15px; fill: var(--brand-orange); }
  .intro-copy { font-family: "Open Sans", sans-serif; font-size: 14.5px; fill: var(--paper-white); }
  .title-light { font-family: "Montserrat", sans-serif; font-weight: 300; font-size: 88px; fill: var(--paper-white); }
  .title-bold { font-family: "Montserrat", sans-serif; font-weight: 700; font-size: 122px; fill: var(--brand-orange); }
  .processing-copy { font-family: "Varela Round", sans-serif; font-size: 13.6px; fill: var(--text-dark); }
  .tech-copy { font-family: "Varela Round", sans-serif; font-size: 13.4px; fill: var(--paper-white); }
  .copy-heading { font-weight: 700; font-family: "Montserrat", sans-serif; }
</style>
</head>
<body>
<svg class="label" viewBox="0 0 1200 1200" xmlns="http://www.w3.org/2000/svg" aria-label="Rundetikett Bitumen Alu Dichtband">
  <defs>
    <clipPath id="outer-disc"><circle cx="600" cy="600" r="566"/></clipPath>
    <clipPath id="ring-disc"><circle cx="600" cy="600" r="541"/></clipPath>
  </defs>

  <!-- label rings -->
  <g class="label-rings">
    <circle cx="600" cy="600" r="566" fill="var(--label-black)"/>
    <circle cx="600" cy="600" r="541" fill="var(--paper-white)"/>
    <rect x="60" y="603" width="1080" height="560" fill="var(--ring-grey)" clip-path="url(#ring-disc)"/>
    <circle cx="600" cy="600" r="491" fill="var(--label-black)"/>
  </g>

  <!-- brand block -->
  <g class="brand-block">
    <rect x="398" y="170" width="82" height="82" fill="none" stroke="var(--brand-orange)" stroke-width="5"/>
    <text class="company-name" x="513" y="186">KORVENT DÄMMSTOFFE GMBH &amp; CO. KG</text>
    <text class="company-contact" x="511" y="206">Lindenweg 14 ,  74000 Musterstadt</text>
    <text class="company-contact" x="511" y="226">Telefon : 06200-48215</text>
    <text class="company-contact" x="511" y="246">Fax :48216</text>
    <text class="company-contact" x="511" y="266">mail: info@korvent-daemmstoffe.de</text>
    <text class="company-contact" x="511" y="286">www.korvent-daemmstoffe.de</text>
  </g>

  <!-- product intro -->
  <g class="intro">
    <text class="intro-copy" x="301" y="322" textLength="605" lengthAdjust="spacing">Das Bitumen Alu Dichtband klebt und dichtet zuverlässig Metall, Kunststoffe,</text>
    <text class="intro-copy" x="283" y="343" textLength="643" lengthAdjust="spacing">monolithische Untergründe, Holz und Glas. Es ist besonders geeignet zum Abdichten</text>
    <text class="intro-copy" x="266" y="364" textLength="678" lengthAdjust="spacing">von: Fugen und Rissen, Regenrinnen, Anschlüssen an Dach und Wand, Abdeckungen,    Glas-</text>
    <text class="intro-copy" x="251" y="386" textLength="710" lengthAdjust="spacing">dächern und Gewächshäusern, Stahlkonstruktionen, Dacheindeckungen, Trauf- und Kehlblechen</text>
  </g>

  <!-- product title -->
  <g class="product-title">
    <text class="title-light" x="415" y="525" textLength="382" lengthAdjust="spacingAndGlyphs">BITUMEN</text>
    <text class="title-bold" x="119" y="647" textLength="953" lengthAdjust="spacingAndGlyphs">ALU DICHTBAND</text>
  </g>

  <!-- technical strip -->
  <polygon class="tech-strip" clip-path="url(#ring-disc)" fill="var(--tape-brown)"
    points="712,843 1125,846 1125,1130 460,1067 456,1005 412,994 408,958 418,932 462,926 712,905"/>

  <!-- processing strip -->
  <polygon class="processing-strip" clip-path="url(#outer-disc)" fill="var(--tape-sand)"
    points="30,697 160,700 162,708 726,698 722,706 733,745 722,800 716,860 713,903 590,912 236,932 30,930"/>

  <g class="processing">
    <text class="processing-copy" x="103" y="731" textLength="577" lengthAdjust="spacing"><tspan class="copy-heading">Verarbeitung:</tspan>   Die zu dichtenden Oberflächen müssen trocken, frost-, fett-</text>
    <text class="processing-copy" x="105" y="749" textLength="575" lengthAdjust="spacing">und silikonfrei sowie abriebfest sein. Poröser oder staubiger Untergrund</text>
    <text class="processing-copy" x="109" y="766" textLength="571" lengthAdjust="spacing">sollte mit Voranstrich (ca. 200ml/m2) vorbehandelt werden, um eine opti-</text>
    <text class="processing-copy" x="116" y="784" textLength="564" lengthAdjust="spacing">male Haftung zu erzielen. Die günstigste Verarbeitungstemperatur liegt</text>
    <text class="processing-copy" x="120" y="802" textLength="560" lengthAdjust="spacing">zwischen 5°C und 45°C, Luft bzw. Oberflächentemperatur. Es wird zur bes-</text>
    <text class="processing-copy" x="125" y="819" textLength="555" lengthAdjust="spacing">seren Haftung im Niedrigtemperaturbereich empfohlen das Bitumen Alu</text>
    <text class="processing-copy" x="133" y="837" textLength="547" lengthAdjust="spacing">Dichtband bei Raumtemperatur zu lagern. Das Bitumen Alu Dichtband</text>
    <text class="processing-copy" x="139" y="855" textLength="541" lengthAdjust="spacing">muss nach dem Aufbringen fest angedrückt werden. Das Entstehen von</text>
    <text class="processing-copy" x="148" y="872" textLength="532" lengthAdjust="spacing">Hohlstellen (Blasen) ist zu vermeiden. Sind mehrere Streifen an zu-</text>
    <text class="processing-copy" x="156" y="890" textLength="524" lengthAdjust="spacing">setzen muss die Überlappung mind. 50 mm betragen. Begehbare- bzw.</text>
    <text class="processing-copy" x="191" y="907" textLength="464" lengthAdjust="spacing">befahrbare Untergründe sind zur Verarbeitung nicht geeignet.</text>
  </g>

  <g class="technical">
    <text class="tech-copy" x="746" y="879" textLength="314" lengthAdjust="spacing"><tspan class="copy-heading">Technische Angaben:</tspan>    Bitumen Alu Di-</text>
    <text class="tech-copy" x="746" y="898" textLength="300" lengthAdjust="spacing">chtband ist ein selbstklebendes und kalt</text>
    <text class="tech-copy" x="746" y="918" textLength="287" lengthAdjust="spacing">zu verarbeitendes Abdichtungsband.</text>
    <text class="tech-copy" x="746" y="937" textLength="272" lengthAdjust="spacing">Die Alufolie ist oberflächenvergütet,</text>
    <text class="tech-copy" x="518" y="956" textLength="485" lengthAdjust="spacing">UV-beständig und hat daher eine    gute mechanische Standfes-</text>
    <text class="tech-copy" x="518" y="975" textLength="469" lengthAdjust="spacing">tigkeit. Die Beschichtungsmasse besteht aus einem hoch werti-</text>
    <text class="tech-copy" x="518" y="994" textLength="451" lengthAdjust="spacing">gen Kunststoff-Harz-Bitumen-Gemisch, welches durch eine</text>
    <text class="tech-copy" x="583" y="1014" textLength="300" lengthAdjust="spacing">silikonbeschichtete Folie geschützt wird.</text>
  </g>
</svg>
</body>
</html>
```